Restaurant Menu Design for Meal Prep offered in a food display cooler at a local Gym

I am looking for a menu design with the following items . I would like a workable copy if possible so in the future we can change pricing on this file , or change items . This file will be uploaded on a USB drive and then plugged into a TV. Please ensure a JPEG file is included so this will also work on this TV.

Have a look at our website , www.vantorelkitchen.com for ideas for design that represent the brand appropriately.
The below are the menu items that we would need displayed along with their pricing.

BREAKFAST MEAL PREP ITEMS
Blueberry Pancakes $12.00
Morning Climb Burrito $10.95

LUNCH/DINNER MEAL PREP OPTIONS
BBQ Glazed Salmon $16.50
Cheeseburger Bowl $13.50
Chicken Alfredo $12.00
Pesto Chicken Pasta $12.00
Chicken Parmesan $13.00
Taco Bowl $14.00
Steak Bite and Green Stir Fry $12.00
Asian Chicken Teriyaki $12.00
Galloway Stir Fry $15.95

I will attach our logo below, this will need to be on the design. The "heading" (for example breakfast meal prep items and lunch/dinner meal prep options) for the menu should also be on the design.

Ive attached a couple of photos that you need to add to your design.

Target Market(s)

This will be displayed in a GYM

Industry/Entity Type

Meal Prep + Fitness Industry

Requirements
Must have
• Vantorel Logo and Photos attached
Nice to have
• Maybe incorporate something that represents working out or healthy lifestyle in design without going too overboard

```html
<!DOCTYPE html>
<html lang="en">
<head>
<meta charset="utf-8">
<title>Vantorel Meal Prep Menu</title>
<link rel="stylesheet" href="https://fonts.googleapis.com/css2?family=Montserrat:wght@600;700;800&family=Questrial&display=swap">
<style>
  :root {
    --page-bg: #f2f2f0;
    --ink: #151515;
    --brand-black: #1e1f1d;
    --brand-green: #8dc63f;
    --band-green: #86bf3a;
    --panel-white: rgba(245, 245, 244, 0.92);
    --wood-light: #e9eaea;
    --wood-mid: #cfd2d3;
    --screen-edge: #111;
  }
  * { margin: 0; padding: 0; box-sizing: border-box; }
  html, body {
    width: 1200px; height: 1000px; overflow: hidden;
    background: var(--page-bg);
  }
  .menu-board {
    position: absolute; left: 40px; top: 120px;
    width: 1120px; height: 760px;
    background: var(--screen-edge);
    padding: 10px;
  }
  .menu-screen {
    position: relative; width: 100%; height: 100%;
    background: linear-gradient(90deg, var(--wood-light), var(--wood-mid) 50%, var(--wood-light));
    overflow: hidden;
    font-family: "Questrial", sans-serif;
    color: var(--ink);
  }
  .brand-block {
    position: absolute; left: 0; top: 0; width: 485px; height: 165px;
    background: var(--brand-black);
    padding: 36px 0 0 66px;
  }
  .brand-name {
    font-family: "Montserrat", sans-serif; font-weight: 700;
    font-size: 52px; letter-spacing: 1px; line-height: 1;
    color: var(--brand-green);
  }
  .brand-tagline {
    margin-top: 10px;
    font-family: "Montserrat", sans-serif; font-weight: 700;
    font-size: 17px; letter-spacing: 0.5px;
    color: var(--brand-green);
  }
  .section-band {
    position: absolute;
    background: var(--band-green);
    font-family: "Montserrat", sans-serif; font-weight: 700;
    color: var(--ink);
    display: flex; align-items: center;
  }
  .breakfast-band { left: 10px; top: 222px; width: 448px; height: 64px; padding-left: 14px; font-size: 22px; }
  .lunch-band { left: 500px; top: 296px; width: 604px; height: 66px; padding-left: 24px; font-size: 23px; }
  .item-panel {
    position: absolute;
    background: var(--panel-white);
  }
  .breakfast-panel { left: 10px; top: 286px; width: 448px; height: 104px; padding: 18px 20px 0 20px; }
  .lunch-panel { left: 500px; top: 362px; width: 604px; height: 378px; padding: 14px 24px 0 24px; }
  .item-list { list-style: none; }
  .item-row {
    display: flex; justify-content: space-between;
    font-size: 22px; line-height: 34px;
  }
  .lunch-panel .item-row { font-size: 23px; line-height: 39.5px; }
  .item-price { font-size: 1.08em; letter-spacing: 0.5px; }
  .photo {
    position: absolute;
  }
  .photo-pancakes {
    left: 500px; top: 0; width: 604px; height: 296px;
    background: radial-gradient(ellipse at 55% 50%, #e4b878 0%, #d29a55 30%, #f3f1ee 62%, #dcdedf 100%);
  }
  .photo-pasta {
    left: 20px; top: 420px; width: 440px; height: 300px;
    background: radial-gradient(ellipse at 50% 45%, #b9a867 0%, #9ea95a 35%, #f6f6f4 62%, #d9dbdc 100%);
  }
</style>
</head>
<body>
  <main class="menu-board">
    <div class="menu-screen">
      <header class="brand-block">
        <div class="brand-name">VANTOREL</div>
        <div class="brand-tagline">HEALTHY KITCHEN &nbsp;|&nbsp; MEAL PREP</div>
      </header>

      <div class="photo photo-pancakes" role="img" aria-label="Stack of blueberry pancakes with yogurt drizzle and fresh blueberries on a white plate"></div>

      <h2 class="section-band breakfast-band">BREAKFAST MEAL PREP ITEMS</h2>
      <section class="item-panel breakfast-panel">
        <ul class="item-list">
          <li class="item-row"><span class="item-name">Blueberry Pancakes</span><span class="item-price">$12.00</span></li>
          <li class="item-row"><span class="item-name">Morning Climb Burrito</span><span class="item-price">$10.95</span></li>
        </ul>
      </section>

      <div class="photo photo-pasta" role="img" aria-label="White bowl of pesto chicken penne pasta with broccoli, red pepper and parmesan"></div>

      <h2 class="section-band lunch-band">LUNCH/DINNER MEAL PREP OPTIONS</h2>
      <section class="item-panel lunch-panel">
        <ul class="item-list">
          <li class="item-row"><span class="item-name">BBQ Glazed Salmon</span><span class="item-price">$16.50</span></li>
          <li class="item-row"><span class="item-name">Cheeseburger Bowl</span><span class="item-price">$13.50</span></li>
          <li class="item-row"><span class="item-name">Chicken Alfredo</span><span class="item-price">$12.00</span></li>
          <li class="item-row"><span class="item-name">Pesto Chicken Pasta</span><span class="item-price">$12.00</span></li>
          <li class="item-row"><span class="item-name">Chicken Parmesan</span><span class="item-price">$13.00</span></li>
          <li class="item-row"><span class="item-name">Taco Bowl</span><span class="item-price">$14.00</span></li>
          <li class="item-row"><span class="item-name">Steak Bite and Green Stir Fry</span><span class="item-price">$12.00</span></li>
          <li class="item-row"><span class="item-name">Asian Chicken Teriyaki</span><span class="item-price">$12.00</span></li>
          <li class="item-row"><span class="item-name">Galloway Stir Fry</span><span class="item-price">$15.95</span></li>
        </ul>
      </section>
    </div>
  </main>
</body>
</html>
```